Design NEW business card

We would like a business card using the colour deep red wine or dark navy blue textured background (patterned or not, open to suggestions) with a high gloss debossed rose gold/copper TM Thomas Marlow Jewellery business name (Provided). I have included images for your review we would like to keep our currently logo and business name on the front but you can change the layout and positioning. For the back of the card we are open to all suggestions/variations.
Use our current TM Thomas Marlow Jewellery logo (Provided image)

```html
<!DOCTYPE html>
<html lang="en">
<head>
<meta charset="utf-8">
<title>Thomas Marlow Jewellery – Business Card</title>
<link href="https://fonts.googleapis.com/css2?family=Open+Sans:wght@400;600&display=swap" rel="stylesheet">
<style>
  :root {
    --backdrop: #3b3430;
    --card-navy: #16203a;
    --card-navy-deep: #0e1628;
    --card-sheen: rgba(255,255,255,.035);
    --rose-gold: #c8916c;
    --ink-light: #f2f2f2;
    --divider: #3a4560;
  }
  * { margin: 0; padding: 0; box-sizing: border-box; }
  html, body {
    width: 1200px; height: 844px; overflow: hidden;
    background: var(--backdrop);
    font-family: "Open Sans", Arial, sans-serif;
  }
  .stage {
    position: relative; width: 1200px; height: 844px;
    display: flex; align-items: center; justify-content: center; gap: 60px;
  }
  .card {
    position: relative; width: 525px; height: 300px;
    background:
      repeating-linear-gradient(45deg, var(--card-sheen) 0 1px, transparent 1px 6px),
      repeating-linear-gradient(-45deg, var(--card-sheen) 0 1px, transparent 1px 6px),
      radial-gradient(ellipse at 40% 35%, var(--card-navy) 0%, var(--card-navy-deep) 100%);
    box-shadow: 0 10px 30px rgba(0,0,0,.45);
  }
  .brand {
    position: absolute; display: flex; align-items: center; gap: 10px;
    color: var(--rose-gold); font-weight: 400; letter-spacing: 2px;
    font-size: 15px; text-transform: uppercase; white-space: nowrap;
  }
  .brand-dot {
    width: 9px; height: 9px; border-radius: 50%; background: var(--rose-gold);
  }
  .card-front .brand { left: 50%; top: 62px; transform: translateX(-50%); }
  .card-back .brand { left: 50%; top: 50%; transform: translate(-50%, -50%); }

  .identity {
    position: absolute; right: 285px; top: 150px; text-align: right;
    color: var(--ink-light);
  }
  .identity .person { color: var(--rose-gold); font-weight: 600; font-size: 21px; line-height: 1.1; }
  .identity .role { font-size: 14px; margin-top: 2px; }
  .identity .address { font-size: 14px; margin-top: 14px; line-height: 1.2; }

  .divider {
    position: absolute; left: 255px; top: 135px; width: 1px; height: 120px;
    background: var(--divider);
  }
  .contacts {
    position: absolute; left: 272px; top: 140px; list-style: none;
    color: var(--ink-light); font-size: 14px;
  }
  .contacts li { display: flex; align-items: center; gap: 10px; height: 22px; white-space: nowrap; }
  .contacts svg { width: 11px; height: 11px; fill: var(--rose-gold); flex: none; }
  .contacts .envelope-flap { fill: none; stroke: var(--card-navy); stroke-width: .9; }
</style>
</head>
<body>
<main class="stage">
  <section class="card card-front" aria-label="Business card front">
    <div class="brand"><span class="brand-dot"></span>Thomas Marlow Jewellery</div>
    <div class="identity">
      <p class="person">Daniel Hartley</p>
      <p class="role">Managing Director</p>
      <p class="address">48 Harbour Lane<br>Bristol, BS1 4QA</p>
    </div>
    <div class="divider"></div>
    <ul class="contacts">
      <li><svg viewBox="0 0 12 12"><path d="M2.5 0.5l2 2-1.2 1.5c.7 1.6 2 2.9 3.7 3.7L8.5 6.5l2 2-1.5 2.5C4.5 10.5 1 7 .5 2z"/></svg>(021)-555-0147</li>
      <li><svg viewBox="0 0 12 12"><rect x="1" y="3" width="10" height="8" rx="1"/><rect x="3" y="1" width="6" height="3"/></svg>555-013-2298</li>
      <li><svg viewBox="0 0 12 12"><rect x="0" y="2" width="12" height="8"/><path class="envelope-flap" d="M0 2l6 4 6-4"/></svg>hello@marlowjewels.com</li>
      <li><svg viewBox="0 0 12 12"><circle cx="6" cy="6" r="5.5"/></svg>www.marlowjewels.com</li>
    </ul>
  </section>
  <section class="card card-back" aria-label="Business card back">
    <div class="brand"><span class="brand-dot"></span>Thomas Marlow Jewellery</div>
  </section>
</main>
</body>
</html>
```